Ink & Toner Postcards (Set of 3)

Postcard
Some Content:

Header Option: STOP Killing your Printer with
Inferior Cartridges

Header Option: STOP Spending TOO MUCH $$ on Cheap Toner Cartridges

Secondary Message" Save Money
with QUALITY Toner Cartridges

Points to Get Across:
Buy Fewer Cartridges, Generate Over 25% (+) Yield
Eliminate Toner Contamination and Reduce Jams
Ensure Top Quality Printing and Printer Reliability
Competitive Prices

To Order, Visit qrvsupplies.com

Special Volume & Bundling Pricing
Call 888-461-2957

Target Market(s)

Small Business Owners
Independent Pharmacies

Industry/Entity Type

Printer

Requirements
Must have
• Phone Number
Website Address
2nd Side B&W, Set Up For Mailing
Output: Adobe Acrobat 9 Document (*.pdf) (recommended)
and
Adobe Illustrator CS3 Artwork (*.ai) (recommended)
or
Adobe Photoshop CS3 Image (*.psd) (recommended)

Full Bleed Size
5.59" x 4.33"
142 x 110 mm
1677 x 1300 pixels

Document Trim Size
5.47" x 4.21"
139 x 107 mm
1642 x 1264 pixels

OR

Full Bleed Size
8.64" x 5.59"
219 x 142 mm
2592 x 1677 pixels

Document Trim Size
8.52" x 5.47"
216 x 139 mm
2556 x 1642 pixels
Should not have
• Too Much Wording, Need Impact of Messaging To Act

```html
<!DOCTYPE html>
<html lang="en">
<head>
<meta charset="utf-8">
<title>Quality Toner Cartridges Postcard</title>
<link href="https://fonts.googleapis.com/css2?family=Source+Sans+3:ital,wght@0,400;1,400;1,700&display=swap" rel="stylesheet">
<style>
  :root {
    --header-blue: #3d88f4;
    --order-blue: #2f7fef;
    --stripe-green: #9ae38a;
    --stripe-blue: #9ec4ff;
    --panel-green: #32d91f;
    --panel-green-dark: #25b416;
    --white: #ffffff;
    --tick-blue: #2a6fe0;
  }
  html, body {
    margin: 0;
    padding: 0;
    width: 1200px;
    height: 923px;
    overflow: hidden;
    background: var(--white);
  }
  .postcard {
    position: relative;
    width: 1200px;
    height: 923px;
    background: var(--white);
    font-family: "Source Sans 3", "Myriad Pro", Arial, sans-serif;
    color: var(--white);
    overflow: hidden;
  }
  .header-band {
    position: absolute;
    left: 0; top: 0;
    width: 1200px; height: 209px;
    background: var(--header-blue);
  }
  .headline {
    position: absolute;
    margin: 0;
    font-style: italic;
    font-weight: 400;
    font-size: 47px;
    line-height: 1;
    white-space: nowrap;
  }
  .headline strong { font-weight: 700; }
  .headline--stop { left: 24px; top: 38px; }
  .headline--save { left: 212px; top: 130px; }

  .stripe { position: absolute; top: 213px; height: 710px; }
  .stripe--green { left: 0; width: 65px; background: var(--stripe-green); }
  .stripe--blue { left: 69px; width: 72px; background: var(--stripe-blue); }

  .texture-panel {
    position: absolute;
    left: 149px; top: 216px;
    width: 1051px; height: 707px;
    background:
      radial-gradient(circle at 30% 40%, rgba(37,180,22,0.35), transparent 60%),
      radial-gradient(circle at 75% 70%, rgba(37,180,22,0.3), transparent 55%),
      var(--panel-green);
  }

  .benefits {
    position: absolute;
    left: 299px; top: 366px;
    margin: 0; padding: 0;
    list-style: none;
  }
  .benefit {
    display: flex;
    align-items: center;
    height: 40px;
    margin-bottom: 48px;
    font-size: 32px;
    white-space: nowrap;
  }
  .benefit__tick { width: 22px; height: 22px; margin-right: 15px; flex: none; }

  .order-box {
    position: absolute;
    left: 14px; top: 819px;
    width: 508px; height: 47px;
    background: var(--order-blue);
    font-size: 32px;
    line-height: 47px;
    text-align: center;
    white-space: nowrap;
  }
  .pricing {
    position: absolute;
    left: 641px; top: 800px;
    font-size: 32px;
    line-height: 43px;
    white-space: nowrap;
  }
</style>
</head>
<body>
<main class="postcard">
  <header class="header-band">
    <h1 class="headline headline--stop"><strong>STOP</strong> Killing your Printer with Inferior Cartridges</h1>
    <h2 class="headline headline--save"><strong>Save</strong> Money with QUALITY Toner Cartridges</h2>
  </header>

  <div class="stripe stripe--green"></div>
  <div class="stripe stripe--blue"></div>
  <div class="texture-panel" role="img" aria-label="Speckled green toner texture background"></div>

  <ul class="benefits">
    <li class="benefit">
      <svg class="benefit__tick" viewBox="0 0 22 22" aria-hidden="true"><rect x="1" y="3" width="18" height="18" fill="#fff"/><path d="M4 12 L9 18 L20 2" fill="none" stroke="var(--tick-blue)" stroke-width="3"/></svg>
      Buy Fewer Cartridges, Generate Over 25% (+) Yield
    </li>
    <li class="benefit">
      <svg class="benefit__tick" viewBox="0 0 22 22" aria-hidden="true"><rect x="1" y="3" width="18" height="18" fill="#fff"/><path d="M4 12 L9 18 L20 2" fill="none" stroke="var(--tick-blue)" stroke-width="3"/></svg>
      Eliminate Toner Contamination and Reduce Jams
    </li>
    <li class="benefit">
      <svg class="benefit__tick" viewBox="0 0 22 22" aria-hidden="true"><rect x="1" y="3" width="18" height="18" fill="#fff"/><path d="M4 12 L9 18 L20 2" fill="none" stroke="var(--tick-blue)" stroke-width="3"/></svg>
      Ensure Top Quality Printing and Printer Reliability
    </li>
    <li class="benefit">
      <svg class="benefit__tick" viewBox="0 0 22 22" aria-hidden="true"><rect x="1" y="3" width="18" height="18" fill="#fff"/><path d="M4 12 L9 18 L20 2" fill="none" stroke="var(--tick-blue)" stroke-width="3"/></svg>
      Competitive Prices
    </li>
  </ul>

  <div class="order-box">To Order, Visit qrvsupplies.com</div>
  <div class="pricing">Special Volume &amp; Bundling Pricing<br>Call 888-461-2957</div>
</main>
</body>
</html>
```